Breast Cancer Awareness Brochure

I need a Breast Cancer Brochure for Medical Clinic for the General population. Please see attached brochures as design templates. I have attached a pdf file with the information to add to the brochure
1. Under stronger together put all the Logos of the sponsors (see attached logos)
2. About breast cancer - add info in PDF file under this section
3. Under check up NOW - Clinic details
ClearVale Medical, 42 Marrow Lane, Basseterre, St. Kitts
Tel # (1 869) 555 0148/ 0149, 555 0172, 555 0190
Bloom Onward TNV Breast Cancer Support Group
# 5 WEFT's Commercial Complex, Basseterre, St. Kitts
Tel# (1 869) 555 0126
email : bloomtnv1997@mailvale.example
website : bloomonwardtnvinc.example

```html
<!DOCTYPE html>
<html lang="en">
<head>
<meta charset="utf-8">
<title>Breast Cancer Awareness Brochure</title>
<link rel="stylesheet" href="https://fonts.googleapis.com/css2?family=Manrope:wght@400;500;600;700;800&family=Oswald:wght@500;600&family=Great+Vibes&display=swap">
<style>
  :root{
    --page:#d9d9d9;
    --magenta:#dd4f9c;
    --rose:#e0509a;
    --rose-soft:#e2609f;
    --blush:#f8c8dd;
    --blush-deep:#eb8fbf;
    --white:#ffffff;
    --ribbon:#ef7fb0;
  }
  *{margin:0;padding:0;box-sizing:border-box}
  html,body{width:720px;height:1200px;overflow:hidden;background:var(--page)}
  body{position:relative;font-family:"Manrope",sans-serif;color:var(--rose)}
  .sheet{position:absolute;left:50px;width:620px;height:439px;display:flex}
  .sheet--outer{top:137px}
  .sheet--inner{top:595px}
  .panel{position:relative;width:206.67px;height:100%;overflow:hidden}
  .panel--magenta{background:var(--magenta);color:var(--white)}
  .panel--cover-left{background:linear-gradient(180deg,#ea8cbd 0%,#f3b3d2 45%,#f7c6dc 100%)}
  .panel--cover-right{background:linear-gradient(180deg,#ea8fbf 0%,#f4bcd6 35%,#f6c4db 100%)}
  .panel--blush{background:var(--blush)}
  .abs{position:absolute}
  .center{left:0;right:0;text-align:center}

  /* cover left */
  .stronger{top:26px;font-size:11px;font-weight:600;color:var(--white)}
  .sponsor{position:absolute;font-size:4.6px;font-weight:700;color:#2a5a9a;white-space:nowrap;transform:translateX(-50%)}
  .rally{top:76px;font-family:"Great Vibes",cursive;font-size:19px;line-height:20px;color:var(--white)}

  /* contact panel */
  .check-title{top:66px;font-size:11px;font-weight:700;line-height:15px}
  .small{font-size:7px;line-height:9px}
  .rule{position:absolute;left:66px;width:75px;height:0.6px;background:rgba(255,255,255,.7)}
  .group-name{top:170px;font-family:"Oswald",sans-serif;font-size:15.5px;font-weight:500;letter-spacing:-.2px}
  .contact-us{top:197px;font-size:10.5px;font-weight:700}
  .icon-row{top:217px;display:flex;justify-content:center;gap:6.5px}
  .icon-row svg{width:20px;height:20px}
  .badge-caption{top:410px;font-family:"Oswald",sans-serif;font-size:6.2px;font-weight:500}

  /* cover right */
  .cover-title{top:52px;font-size:19px;font-weight:800;line-height:23px;color:var(--rose);letter-spacing:-.2px}
  .cover-sub{top:103px;font-size:10px;line-height:12.5px;color:var(--rose-soft)}

  /* inner panels */
  .content{position:absolute;left:25px;right:18px}
  .h2{font-size:12px;font-weight:700;color:var(--rose);letter-spacing:-.1px}
  .panel--magenta .h2{color:var(--white)}
  .body{font-size:7px;line-height:8.9px;color:var(--rose-soft)}
  .h3{font-size:7.3px;font-weight:700;color:var(--rose)}
  .list{list-style:none;font-size:7px;line-height:8.9px}
  .list li{position:relative;padding-left:6px;margin-top:4.3px}
  .list li::before{content:"•";position:absolute;left:0}
  .panel--blush .list{color:var(--rose-soft)}
  .art{position:absolute}
</style>
</head>
<body>

<!-- OUTSIDE -->
<section class="sheet sheet--outer">
  <div class="panel panel--cover-left">
    <p class="abs center stronger">Stronger Together</p>
    <span class="sponsor" style="left:101px;top:59px">Dawnleaf Pharmacy</span>
    <span class="sponsor" style="left:45px;top:80px">Clearbrook Water</span>
    <span class="sponsor" style="left:163px;top:80px">Palm Cove Apparel</span>
    <span class="sponsor" style="left:41px;top:124px">Ridgeline Springs</span>
    <span class="sponsor" style="left:167px;top:125px">Tamarind Bar</span>
    <span class="sponsor" style="left:63px;top:165px">ClearVale Medical</span>
    <span class="sponsor" style="left:146px;top:165px">Wellmark Pharmacy</span>
    <p class="abs center rally">Join Us<br>In The Fight<br>Against<br>Breast Cancer</p>
    <div class="art" role="img" aria-label="Illustration of a woman in a pink top with an awareness ribbon, with a flowing pink ribbon behind her"
         style="left:0;top:225px;width:207px;height:214px;background:linear-gradient(160deg,#f4a9cb 0%,#f09ac2 40%,#ee6fa5 100%);border-radius:60px 60px 0 0"></div>
  </div>

  <div class="panel panel--magenta">
    <p class="abs center check-title">Check Up NOW!<br>ClearVale Medical</p>
    <p class="abs center small" style="top:101px">42 Marrow Lane, Basseterre, St. Kitts</p>
    <span class="rule" style="top:113px"></span>
    <p class="abs center small" style="top:119px">(1 869) 555 0148 / 0149<br>555 0172, 555 0190</p>
    <p class="abs center group-name">BLOOM ONWARD TNV</p>
    <p class="abs center contact-us">CONTACT US</p>
    <div class="abs center icon-row">
      <svg viewBox="0 0 20 20" aria-label="Address"><circle cx="10" cy="10" r="9.3" fill="#ea7fb5" stroke="#fff" stroke-width=".8"/><path d="M10 5.5a2.8 2.8 0 0 0-2.8 2.8c0 2.1 2.8 5.2 2.8 5.2s2.8-3.1 2.8-5.2A2.8 2.8 0 0 0 10 5.5z" fill="none" stroke="#fff" stroke-width=".8"/><circle cx="10" cy="8.3" r="1" fill="none" stroke="#fff" stroke-width=".7"/></svg>
      <svg viewBox="0 0 20 20" aria-label="Phone"><circle cx="10" cy="10" r="9.3" fill="#ea7fb5" stroke="#fff" stroke-width=".8"/><path d="M7 5.8l1.5 2-1 1.2a6 6 0 0 0 3.5 3.5l1.2-1 2 1.5-.9 1.6c-3.8-.2-7-3.4-7.2-7.2z" fill="none" stroke="#fff" stroke-width=".8" stroke-linejoin="round"/></svg>
      <svg viewBox="0 0 20 20" aria-label="Email"><circle cx="10" cy="10" r="9.3" fill="#ea7fb5" stroke="#fff" stroke-width=".8"/><rect x="6" y="7" width="8" height="6" fill="none" stroke="#fff" stroke-width=".8"/><path d="M6 7l4 3.2L14 7" fill="none" stroke="#fff" stroke-width=".8"/></svg>
      <svg viewBox="0 0 20 20" aria-label="Website"><circle cx="10" cy="10" r="9.3" fill="#ea7fb5" stroke="#fff" stroke-width=".8"/><circle cx="10" cy="10" r="4.2" fill="none" stroke="#fff" stroke-width=".8"/><ellipse cx="10" cy="10" rx="1.8" ry="4.2" fill="none" stroke="#fff" stroke-width=".7"/><path d="M5.8 10h8.4" stroke="#fff" stroke-width=".7"/></svg>
    </div>
    <p class="abs center small" style="top:247px">5 WEFT's Commercial Complex,<br>Basseterre, St. Kitts</p>
    <span class="rule" style="top:270px"></span>
    <p class="abs center small" style="top:274px">(1 869) 555 0126</p>
    <span class="rule" style="top:287px;left:55px;width:97px"></span>
    <p class="abs center small" style="top:292px">bloomtnv1997@mailvale.example</p>
    <span class="rule" style="top:305px;left:55px;width:97px"></span>
    <p class="abs center small" style="top:310px">bloomonwardtnvinc.example</p>
    <svg class="abs" style="left:70px;top:337px" width="67" height="67" viewBox="0 0 67 67" aria-hidden="true"><circle cx="33.5" cy="33.5" r="32" fill="#fff" stroke="#ea7fb5" stroke-width="2"/></svg>
    <p class="abs center badge-caption">BREAST CANCER SUPPORT GROUPS</p>
  </div>

  <div class="panel panel--cover-right">
    <h1 class="abs center cover-title">BREAST CANCER<br>AWARENESS</h1>
    <p class="abs center cover-sub">Together for Women’s<br>Health in St. Kitts &amp; Nevis</p>
    <div class="art" role="img" aria-label="Large looping pink awareness ribbon above a woman holding a pink ribbon to her chest"
         style="left:0;top:160px;width:207px;height:279px;background:linear-gradient(170deg,#f3a7c9 0%,#ef86b6 45%,#f6c0d8 100%);border-radius:90px 90px 0 0"></div>
  </div>
</section>

<!-- INSIDE -->
<section class="sheet sheet--inner">
  <div class="panel panel--blush">
    <div class="content" style="top:24px">
      <h2 class="h2">What is Breast Cancer?</h2>
      <p class="body" style="margin-top:5px">Breast cancer is a disease in which abnormal cells in the breast grow out of control, forming a lump or tumor. It is the most common cancer among women worldwide, and it can also (rarely) affect men.</p>
      <h3 class="h3" style="margin-top:21px">Key Facts &amp; Statistics</h3>
      <p class="body" style="margin-top:5px">Global: 2.3 million women diagnosed in 2020; 670,000 deaths; 1 in 8 women will be diagnosed in their lifetime.</p>
      <p class="body" style="margin-top:9px">Caribbean: Leading cancer in women, often diagnosed at later stages, higher mortality rates than in high-income countries.</p>
      <p class="body" style="margin-top:9px">St. Kitts &amp; Nevis: 25 new cases in 2019; breast cancer is the leading cancer among women.</p>
    </div>
    <div class="art" role="img" aria-label="Watercolour pink awareness ribbon with leaves, flowers and a butterfly"
         style="left:0;top:268px;width:207px;height:171px;background:radial-gradient(ellipse at 55% 55%,#f08bb9 0%,#f5aacb 50%,var(--blush) 80%)"></div>
  </div>

  <div class="panel panel--magenta">
    <div class="content" style="top:24px;left:21px">
      <h2 class="h2">Risk Factors</h2>
      <ul class="list" style="margin-top:1px">
        <li>Age (risk increases with age)</li>
        <li>Family history of breast cancer</li>
        <li>Genetic mutations (BRCA1, BRCA2)</li>
        <li>Hormonal factors (early menstruation,<br>late menopause)</li>
        <li>Lifestyle (obesity, smoking, alcohol use,<br>lack of exercise)</li>
      </ul>
      <h2 class="h2" style="margin-top:11px">Signs &amp; Symptoms</h2>
      <ul class="list" style="margin-top:1px">
        <li>Lump in the breast or underarm</li>
        <li>Change in breast size or shape</li>
        <li>Nipple discharge or inversion</li>
        <li>Skin changes (dimpling, redness, thickening)</li>
        <li>Persistent breast pain</li>
      </ul>
      <h2 class="h2" style="margin-top:11px">Prevention &amp; Early Detection</h2>
      <ul class="list" style="margin-top:1px">
        <li>Regular mammograms from age 40+<br>(earlier if high risk)</li>
        <li>Monthly breast self-checks</li>
        <li>Healthy lifestyle: balanced diet, exercise,<br>limit alcohol, avoid smoking</li>
        <li>Genetic testing for high-risk individuals</li>
      </ul>
    </div>
    <div class="art" role="img" aria-label="Pink ribbon sweeping across the bottom of the panel"
         style="left:0;top:385px;width:207px;height:54px;background:linear-gradient(180deg,rgba(248,200,221,0) 0%,#f3a2c6 60%,#ef86b6 100%)"></div>
  </div>

  <div class="panel panel--blush">
    <div class="content" style="top:24px;left:24px">
      <h2 class="h2">Treatment Options</h2>
      <ul class="list" style="margin-top:1px">
        <li>Surgery (lumpectomy, mastectomy)</li>
        <li>Radiation therapy</li>
        <li>Chemotherapy</li>
        <li>Hormone therapy</li>
        <li>Targeted therapy &amp; immunotherapy</li>
      </ul>
      <h2 class="h2" style="margin-top:21px">Hope &amp; Support</h2>
      <p class="body" style="margin-top:3px">Survival rates have improved significantly with early detection. Many survivors lead healthy, fulfilling lives after treatment. Support groups and counseling are available for patients and families.</p>
    </div>
    <div class="art" role="img" aria-label="Illustration of a woman in a pink top doing a breast self-check, framed by green leaves"
         style="left:0;top:228px;width:207px;height:211px;background:linear-gradient(160deg,#f6d3dc 0%,#f4b9c9 45%,#ee7fa6 100%);border-radius:80px 0 0 0"></div>
  </div>
</section>

</body>
</html>
```